Fitness Equipment & Service

I want to make the card eye catching and fun. We are called Copperleaf Motion Limited and we are based in Wales. We sell, install and service all types of fitness equipment from Skipping ropes, right through the Dumbbells, Kettle bells and Barbells through to state of the art Treadmills, Running Machines and Strength Equipment. We also design and install changing room furniture and lockers.

TYPOGRAPHY
We would like to use Futrura. Futura has an appearance of efficiency and forwardness. The typeface is derived
from simple geometric forms (near-perfect circles, triangles and squares) and is based on strokes of
near-even weight, which are low in contrast. This is most visible in the almost perfectly round stroke of
the o, which is nonetheless slightly ovoid.
The lowercase has tall ascenders, which rise above the cap line. The uppercase
characters present proportions similar to those of classical Roman capitals.

TYPOGRAPHIC CONSIDERATIONS
No Strike though
No Horizontal Scaling
No Drop Shadows
No Effects
Never use less than 120% Leading

OUR CORPORATE COLOURS
BRAND GUIDELINES
We were thinking that our primary colour palette consists of the Acid Green (Pantone 382) and Process Black.

We work closely with torvane Ltd and would like to include their name on the card somewhere. I have attached images of the other brands that we work with as an idea or the small icons I have included that illustrate what we do?. I have very kindly been given permission to use any of the images off the files that I have included below, so I hope these help. I will include these below. I would be open to suggestions if it made the card more striking Can you do it?

Hi All, Just wanted to add a few thoughts but you are the guys with the creative visions (thats why are here) We are based in Wales, UK and we would be open to lots of different ideas on a theme but must be eye catching, Bold and FUN. If you can or think that the Welsh or any dragon could be put in there then go for it (its not a must have) We have also added some ideas for colour but again its over to you!! GO FOR IT ! Thanks and look forward to your visions! Owen

Hi All, Just thought I would sen through the contact details that need to be on the card. (if you want to play around with icons instead of the wording twitter, Facebook, go for it): Copperleaf Motion Limited Owen Pritchard Managing Director Mob: +44 (0)7391 508 262 e-mail: sales@copperleafmotion.co.uk Web: Copperleafmotion.co.uk twitter: @motionParcelbin Facebook: Copperleaf Motion Limited

```html
<!DOCTYPE html>
<html lang="en">
<head>
<meta charset="utf-8">
<title>Copperleaf Motion Limited – Business Card</title>
<link rel="stylesheet" href="https://fonts.googleapis.com/css2?family=Open+Sans:wght@400;600;700&display=swap">
<style>
  :root {
    --backdrop: #2b2b2d;
    --card-white: #eeeeef;
    --card-shadow: rgba(0,0,0,0.45);
    --navy: #0d1a4a;
    --brand-blue: #1f3d8a;
    --text-grey: #3a3f55;
    --rule-grey: #c9cacd;
    --gold: #d9a53a;
    --collage-deep: #0f2a66;
    --collage-mid: #2a5aa8;
    --collage-light: #7f9cc8;
    --tile-a: rgba(10, 30, 80, 0.55);
    --tile-b: rgba(60, 100, 170, 0.55);
    --tile-c: rgba(150, 170, 210, 0.55);
    --tile-d: rgba(30, 140, 200, 0.5);
  }
  * { margin: 0; padding: 0; box-sizing: border-box; }
  html, body { width: 1200px; height: 900px; overflow: hidden; }
  body {
    background: var(--backdrop);
    font-family: "Open Sans", Arial, sans-serif;
    position: relative;
  }
  .card {
    position: absolute;
    top: 300px;
    width: 520px;
    height: 300px;
    border-radius: 22px;
    overflow: hidden;
    box-shadow: 0 14px 30px var(--card-shadow);
  }
  /* Front */
  .card-front { left: 50px; background: var(--card-white); }
  .brand-block {
    position: absolute;
    left: 30px; top: 60px;
    width: 200px;
    display: flex; flex-direction: column; align-items: center;
  }
  .brand-disc {
    width: 120px; height: 120px; border-radius: 50%;
    background: radial-gradient(circle at 40% 35%, var(--collage-mid), var(--navy));
    border: 4px solid #fff;
    box-shadow: 0 0 0 1px var(--rule-grey);
  }
  .brand-name {
    margin-top: 16px;
    font-size: 15px; font-weight: 700; line-height: 1.25;
    color: var(--navy); text-align: center;
  }
  .divider {
    position: absolute; left: 248px; top: 40px;
    width: 1px; height: 200px; background: var(--rule-grey);
  }
  .contact { position: absolute; left: 272px; top: 58px; }
  .person-name { font-size: 17px; font-weight: 700; color: var(--brand-blue); line-height: 1.2; }
  .person-role { font-size: 12px; color: var(--text-grey); line-height: 1.3; margin-bottom: 22px; }
  .contact-list { list-style: none; }
  .contact-list li {
    display: flex; align-items: center; gap: 8px;
    font-size: 12px; color: var(--text-grey); line-height: 1.45;
  }
  .contact-list svg { width: 10px; height: 10px; flex: none; fill: var(--brand-blue); }
  /* Back */
  .card-back { left: 630px; }
  .back-collage {
    position: absolute; inset: 0;
    background: linear-gradient(135deg, var(--collage-deep) 0%, var(--collage-mid) 55%, var(--collage-light) 100%);
  }
  .tile-grid {
    position: absolute; inset: -6px;
    display: grid;
    grid-template-columns: repeat(8, 1fr);
    grid-template-rows: repeat(5, 1fr);
    gap: 3px;
  }
  .tile { background: var(--tile-a); }
  .tile.mid { background: var(--tile-b); }
  .tile.light { background: var(--tile-c); }
  .tile.cyan { background: var(--tile-d); }
  .tile.clear { background: transparent; }
  .back-badge {
    position: absolute; left: 38%; top: 56%;
    transform: translate(-50%, -50%);
    width: 190px; height: 190px; border-radius: 50%;
    background: var(--navy);
    border: 5px solid #fff;
    display: flex; align-items: center; justify-content: center;
    text-align: center; padding: 24px;
  }
  .back-badge span { font-size: 18px; font-weight: 700; line-height: 1.3; color: var(--gold); }
</style>
</head>
<body>
  <section class="card card-front">
    <div class="brand-block">
      <div class="brand-disc"></div>
      <p class="brand-name">Copperleaf Motion Limited</p>
    </div>
    <div class="divider"></div>
    <div class="contact">
      <p class="person-name">Owen Pritchard</p>
      <p class="person-role">Managing Director</p>
      <ul class="contact-list">
        <li><svg viewBox="0 0 10 10"><path d="M2 0.5 L4 2.5 L3 4 Q4.5 6 6 7 L7.5 6 L9.5 8 L8 9.5 Q3 9 0.5 2 Z"/></svg>+44 (0)7391 508 262</li>
        <li><svg viewBox="0 0 10 10"><rect x="0.5" y="2" width="9" height="6.5" rx="0.8"/><path d="M0.8 2.4 L5 5.6 L9.2 2.4" stroke="#eeeeef" stroke-width="0.9" fill="none"/></svg>sales@copperleafmotion.co.uk</li>
        <li><svg viewBox="0 0 10 10"><circle cx="5" cy="5" r="4.5"/><path d="M0.5 5 H9.5 M5 0.5 V9.5 M5 0.5 Q2 5 5 9.5 Q8 5 5 0.5" stroke="#eeeeef" stroke-width="0.7" fill="none"/></svg>Copperleafmotion.co.uk</li>
        <li><svg viewBox="0 0 10 10"><path d="M1 1.5 H9 Q9.5 1.5 9.5 2 V6.5 Q9.5 7 9 7 H4 L1.8 9 V7 H1 Q0.5 7 0.5 6.5 V2 Q0.5 1.5 1 1.5 Z"/></svg>@motionParcelbin</li>
        <li><svg viewBox="0 0 10 10"><circle cx="5" cy="3" r="2.2"/><path d="M0.8 9.5 Q0.8 5.8 5 5.8 Q9.2 5.8 9.2 9.5 Z"/></svg>Copperleaf Motion Limited</li>
      </ul>
    </div>
  </section>

  <section class="card card-back">
    <div class="back-collage" role="img" aria-label="Collage of gym photographs in blue tones behind a grid of tiles with white fitness service icons">
      <div class="tile-grid">
        <div class="tile"></div><div class="tile mid"></div><div class="tile clear"></div><div class="tile light"></div><div class="tile"></div><div class="tile mid"></div><div class="tile cyan"></div><div class="tile light"></div>
        <div class="tile clear"></div><div class="tile"></div><div class="tile light"></div><div class="tile mid"></div><div class="tile clear"></div><div class="tile light"></div><div class="tile"></div><div class="tile mid"></div>
        <div class="tile mid"></div><div class="tile light"></div><div class="tile"></div><div class="tile clear"></div><div class="tile light"></div><div class="tile"></div><div class="tile mid"></div><div class="tile clear"></div>
        <div class="tile light"></div><div class="tile clear"></div><div class="tile mid"></div><div class="tile"></div><div class="tile mid"></div><div class="tile clear"></div><div class="tile light"></div><div class="tile cyan"></div>
        <div class="tile"></div><div class="tile mid"></div><div class="tile clear"></div><div class="tile light"></div><div class="tile"></div><div class="tile mid"></div><div class="tile"></div><div class="tile light"></div>
      </div>
    </div>
    <div class="back-badge"><span>Copperleaf Motion Limited</span></div>
  </section>
</body>
</html>
```